Electrical business needs a flyer design

we need a Trifold flyer designed for an electrical company. Our service include new installations, renovations and rewires, safety checks, switchboard upgrades, services and breakdown, home automation and power monitoring. we would like to see designs using dark grey, orange and blue. the final designs should communicate a friendly but professional service. I have attached my old business brochure to indicate the service we provide
Target Market(s)
home owners
Industry/Entity Type
Electrical
Look and feel
Each slider illustrates characteristics of the customer's brand and the style your logo design should communicate.

```html
<!DOCTYPE html>
<html lang="en">
<head>
<meta charset="utf-8">
<title>Ridgeline Electrical – Trifold Flyer</title>
<link href="https://fonts.googleapis.com/css2?family=Lato:wght@400;700;900&display=swap" rel="stylesheet">
<style>
  :root{
    --orange:#f47b20;
    --blue:#2196e0;
    --blue-deep:#1a7fc8;
    --blue-soft:#7cbfea;
    --ink:#3a3f44;
    --grey:#7b8086;
    --paper:#ffffff;
    --mist:#eef1f4;
    --photo:#c9cfd6;
    --stage:#e4e4e4;
  }
  *{box-sizing:border-box;margin:0;padding:0}
  html,body{width:848px;height:1200px;overflow:hidden}
  body{background:var(--stage);font-family:'Lato',sans-serif;color:var(--ink);position:relative}
  .sheet{position:absolute;left:31px;width:791px;background:var(--paper);overflow:hidden}
  .sheet--outside{top:31px;height:568px}
  .sheet--inside{top:623px;height:550px}
  .panel{position:absolute;top:0;height:100%}
  .art{position:absolute;inset:0}

  /* outside */
  .emergency{left:0;width:264px;background:var(--orange);color:#fff;padding:190px 22px 0 26px}
  .emergency h2{font-size:17px;font-weight:700;line-height:1.3;margin-bottom:16px}
  .emergency p{font-size:12.5px;line-height:1.35;margin-bottom:14px}
  .about{left:264px;width:251px;padding:24px 20px 0;text-align:center}
  .brand{display:inline-flex;align-items:center;gap:6px;font-weight:900;color:var(--blue-deep);letter-spacing:.5px}
  .brand__dot{width:12px;height:12px;border-radius:50%;background:var(--orange)}
  .about .brand{font-size:13px;margin-bottom:22px}
  .about__lead{color:var(--blue);font-weight:700;font-size:16.5px;line-height:1.3;margin-bottom:16px}
  .about__body{font-size:12px;line-height:1.4;margin-bottom:24px}
  .contact__title{color:var(--orange);font-weight:700;font-size:16px;margin-bottom:12px}
  .contact{list-style:none;text-align:left}
  .contact li{display:flex;align-items:flex-start;gap:10px;font-size:11px;line-height:1.35;margin-bottom:14px}
  .contact svg{flex:none}
  .contact strong{font-weight:700}
  .cover{left:515px;width:276px}
  .cover .brand{position:absolute;top:180px;left:0;right:0;justify-content:center;font-size:19px}
  .cover__tag{position:absolute;right:22px;top:436px;text-align:right;color:#fff}
  .cover__tag small{display:block;font-size:12px;line-height:1.3;margin-bottom:4px}
  .cover__tag strong{display:block;font-size:16px;font-weight:400;line-height:1.25}

  /* inside */
  .services{position:absolute;font-size:13px;color:var(--grey)}
  .services h3{font-size:22px;font-weight:700;color:var(--ink);line-height:1.15;margin-bottom:12px}
  .services__kicker{font-size:15px;margin-bottom:2px}
  .services ul{list-style:none;line-height:1.35}
  .services--electrical{left:297px;top:44px;width:190px}
  .services--comms{left:550px;top:180px;width:220px}
  .inside-brand{position:absolute;left:550px;top:92px;width:220px;justify-content:center}
  .inside-brand.brand{display:flex;font-size:15px}
  .focus{position:absolute;left:22px;top:268px;width:226px;color:#fff}
  .focus h2{font-size:19.5px;font-weight:700;line-height:1.3;margin-bottom:14px}
  .focus p{font-size:11.5px;line-height:1.4;margin-bottom:12px}
  .focus p.focus__note{font-weight:700}
  .cta{position:absolute;left:335px;top:392px;width:170px;text-align:center;color:#fff}
  .cta strong{display:block;font-size:19px;font-weight:700;margin-bottom:2px}
  .cta span{display:block;font-size:14px;line-height:1.25}
</style>
</head>
<body>

<section class="sheet sheet--outside">
  <div class="panel emergency">
    <h2>We offer a 24-hour, seven-day emergency response service</h2>
    <p>when you need an electrician due to a breakdown or other disruption to your power supply.</p>
    <p>Our electrical contractor will identify the fault and have your power back on as soon as possible.</p>
  </div>

  <div class="panel about">
    <div class="brand"><span class="brand__dot"></span>RIDGELINE ELECTRICAL</div>
    <p class="about__lead">Ridgeline is privately owned business providing a comprehensive range of domestic, commercial and industrial electrical services including small jobs around the home to large industrial applications</p>
    <p class="about__body">Our business is underpinned by commitment to customer service, that is, we turn up on time providing quality workmanship at a fair and competitive price.</p>
    <h3 class="contact__title">Get In Touch</h3>
    <ul class="contact">
      <li>
        <svg width="22" height="22" viewBox="0 0 22 22"><circle cx="11" cy="11" r="11" fill="var(--blue)"/><circle cx="11" cy="9" r="3.4" fill="none" stroke="#fff" stroke-width="1.6"/><path d="M11 12.5v5" stroke="#fff" stroke-width="1.6"/></svg>
        <span><strong>Dan Fielding</strong><br>PO BOX 4410 Whyalla SA 5600</span>
      </li>
      <li>
        <svg width="22" height="22" viewBox="0 0 22 22"><circle cx="11" cy="11" r="11" fill="var(--blue)"/><rect x="6" y="8" width="10" height="7" rx="1.5" fill="#fff"/><path d="M6.5 8.5c1-2 8-2 9 0" stroke="#fff" stroke-width="1.6" fill="none"/></svg>
        <span>0400 127 386 (phone)<br>8600 4172 (fax)</span>
      </li>
      <li>
        <svg width="22" height="22" viewBox="0 0 22 22"><circle cx="11" cy="11" r="11" fill="var(--blue)"/><rect x="6" y="7.5" width="10" height="7" fill="none" stroke="#fff" stroke-width="1.4"/><path d="M6 7.5l5 4 5-4" fill="none" stroke="#fff" stroke-width="1.4"/></svg>
        <span>dfielding.electric@example.com</span>
      </li>
    </ul>
  </div>

  <div class="panel cover">
    <svg class="art" viewBox="0 0 276 568" preserveAspectRatio="none">
      <rect width="276" height="568" fill="var(--photo)" role="img" aria-label="Photograph of an electrician's hands working on wiring inside a switchboard"/>
      <rect width="276" height="568" fill="#fff" opacity=".55"/>
      <polygon points="0,392 276,322 276,346 0,416" fill="var(--blue)"/>
      <polygon points="0,416 276,346 276,568 0,568" fill="var(--orange)"/>
    </svg>
    <div class="brand"><span class="brand__dot"></span>RIDGELINE ELECTRICAL</div>
    <div class="cover__tag">
      <small>Accredited<br>Master Electricians</small>
      <strong>FOR ALL YOUR<br>ELECTRICAL NEEDS</strong>
    </div>
  </div>
</section>

<section class="sheet sheet--inside">
  <svg class="art" viewBox="0 0 791 550" preserveAspectRatio="none">
    <defs>
      <linearGradient id="blueFade" x1="0" y1="0" x2="1" y2="0">
        <stop offset="0" stop-color="var(--blue)"/>
        <stop offset=".6" stop-color="var(--blue)"/>
        <stop offset="1" stop-color="var(--blue-soft)"/>
      </linearGradient>
    </defs>
    <rect width="791" height="550" fill="var(--mist)" role="img" aria-label="Faded photograph of an electrician working at a distribution board"/>
    <rect x="264" width="2" height="550" fill="#fff"/>
    <rect x="515" width="2" height="550" fill="#fff"/>
    <polygon points="0,0 264,0 264,249 0,182" fill="var(--photo)" role="img" aria-label="Photograph of a smiling electrician in a hard hat on a yellow ladder"/>
    <polygon points="0,182 791,380 791,418 0,218" fill="var(--orange)"/>
    <polygon points="0,218 791,418 791,550 0,550" fill="url(#blueFade)"/>
    <polygon points="284,428 330,392 330,470" fill="var(--orange)"/>
    <polygon points="402,482 472,478 440,532" fill="var(--orange)"/>
  </svg>

  <div class="services services--electrical">
    <p class="services__kicker">What We Do</p>
    <h3>ELECTRICAL<br>SERVICES :</h3>
    <ul>
      <li>- New Installations</li>
      <li>- Renovation and Re-wiring</li>
      <li>- Installation of Safety Switches</li>
      <li>- Switchboard Upgrades</li>
      <li>- Services and Break Downs</li>
    </ul>
  </div>

  <div class="brand inside-brand"><span class="brand__dot"></span>RIDGELINE ELECTRICAL</div>

  <div class="services services--comms">
    <h3>COMMUNICATION<br>SERVICES :</h3>
    <ul>
      <li>- New Installations</li>
      <li>- Additional Phone and Data Points</li>
      <li>- Antennas and TV Points</li>
      <li>- LAN Setup</li>
    </ul>
  </div>

  <div class="focus">
    <h2>Our focuses are on providing our customers with the best possible service available.</h2>
    <p>Our trade people are higly qualified to ensure quality and realibility. We strive to continually change and grow within the industry.</p>
    <p class="focus__note">We are constanly making change to serve you better.</p>
  </div>

  <div class="cta">
    <strong>CALL US TODAY!</strong>
    <span>For a <b>Free</b><br>No Obligation Quote</span>
  </div>
</section>

</body>
</html>
```